Medical Call Centre Needs a Web Design

We need a web design for a new company based in Melbourne called "Clinora Services". We provide medical centres with administrative support by managing inbound calls to our clients facility. We require a clean, simple and easy to navigate website with an ultimate end product alike this - http://www.plumevanta.com/

The final design should communicate professionalism, new age and inovative.

Industry/Entity Type

It Company

```html
<!DOCTYPE html>
<html lang="en">
<head>
<meta charset="utf-8">
<title>Clinora Services</title>
<link href="https://fonts.googleapis.com/css2?family=Roboto:wght@400;500;700&display=swap" rel="stylesheet">
<style>
:root{
  --red:#c70d2e;
  --red-dark:#a90b27;
  --red-nav:#b30c2a;
  --yellow:#f4c232;
  --ink:#111;
  --muted:#888;
  --light:#f8f8f8;
  --white:#fff;
  --caption:rgba(20,20,20,.85);
}
*{margin:0;padding:0;box-sizing:border-box}
html,body{width:1200px;height:2185px;overflow:hidden}
body{font-family:"Roboto",Arial,sans-serif;color:var(--ink);background:var(--white);position:relative}
.abs{position:absolute}
.y{color:var(--yellow)}
.r{color:var(--red)}

/* header */
.site-header{position:absolute;left:0;top:0;width:1200px;height:190px;background:var(--red)}
.brand{left:171px;top:28px;font-size:40px;font-weight:400;color:var(--white);letter-spacing:-.5px}
.social-top{left:893px;top:36px;display:flex;gap:11px}
.social-top span{width:39px;height:39px;border:2px solid var(--white);border-radius:50%;display:block}
.main-nav{left:171px;top:120px;height:70px;display:flex}
.main-nav a{width:127px;height:70px;display:flex;align-items:center;justify-content:center;color:var(--white);text-decoration:none;font-size:23px;background:var(--red-nav);border-right:1px solid var(--red-dark)}
.main-nav a.active{background:var(--white);color:var(--red)}
.nav-phone{left:807px;top:120px;width:221px;height:70px;background:var(--yellow);color:var(--white);display:flex;align-items:center;justify-content:center;gap:10px;font-size:26px}

/* hero */
.hero{position:absolute;left:0;top:190px;width:1200px;height:404px;background:var(--white)}
.hero h1{left:171px;top:110px;font-size:47px;font-weight:400;line-height:1.15;letter-spacing:-.5px}
.hero h1 .line2{display:block;font-weight:500;font-size:51px;margin-top:12px}
.btn-more{left:171px;top:251px;width:159px;height:56px;background:var(--red);color:var(--white);font-size:24px;display:flex;align-items:center;justify-content:center;border-radius:3px}
.hero-visual{left:728px;top:20px;width:300px;height:384px;background:linear-gradient(180deg,#eef0f2 0%,#dfe5ea 60%,#c8d2da 100%);border-radius:150px 150px 0 0}
.slider-arrow{top:190px}
.slider-dots{left:172px;top:382px;display:flex;gap:5px}
.slider-dots i{width:8px;height:8px;border-radius:50%;background:#ddd;display:block}
.slider-dots i:first-child{background:#777}

/* features */
.features{position:absolute;left:0;top:594px;width:1200px;height:256px;background:var(--red);display:flex;justify-content:center}
.feature{width:286px;text-align:center;color:var(--white);padding-top:43px}
.feature svg{height:64px;display:block;margin:0 auto}
.feature h3{font-size:23px;font-weight:400;margin-top:26px}
.feature p{font-size:13px;line-height:18px;margin-top:12px;white-space:nowrap}

/* why + faq */
.info{position:absolute;left:0;top:850px;width:1200px;height:447px;background:var(--white)}
.sec-title{font-size:37px;font-weight:400;display:flex;align-items:center;gap:12px}
.why-title{left:173px;top:30px}
.why-item{left:173px;display:flex;align-items:flex-start;gap:22px}
.why-item .disc{width:91px;height:91px;border-radius:50%;background:var(--red);box-shadow:0 0 0 4px #f3c5cd;display:flex;align-items:center;justify-content:center;flex-shrink:0}
.why-item h4{font-size:23px;font-weight:400;margin-top:10px}
.why-item p{font-size:13px;line-height:20px;color:var(--muted);margin-top:6px;white-space:nowrap}
.faq-title{left:690px;top:30px}
.faq{left:690px;width:338px}
.faq-row{display:flex;height:47px;margin-bottom:11px}
.faq-row .toggle{width:58px;background:var(--yellow);color:var(--white);font-size:26px;display:flex;align-items:center;justify-content:center}
.faq-row .q{flex:1;background:var(--red);color:var(--white);font-size:14px;display:flex;align-items:center;padding-left:24px}
.faq-open{margin-top:-11px;margin-bottom:11px;height:95px;background:var(--light);padding:12px 20px 0 72px;font-size:12.5px;line-height:18px;color:var(--muted)}

/* services */
.services{position:absolute;left:0;top:1297px;width:1200px;height:357px;background:var(--light)}
.center-title{width:1200px;left:0;text-align:center;font-size:39px;font-weight:500;letter-spacing:-.3px}
.card{top:100px;width:255px;height:224px;border:1px solid #ddd;overflow:hidden}
.card .photo{width:100%;height:100%}
.card p{position:absolute;left:0;bottom:0;width:100%;height:64px;background:var(--caption);color:var(--white);font-size:11.5px;line-height:19px;padding:13px 0 0 12px;white-space:nowrap}

/* clients */
.clients{position:absolute;left:0;top:1654px;width:1200px;height:253px;background:var(--white)}
.client{top:91px;width:177px;height:127px;border:1px solid #e6e6e6;display:flex;align-items:center;justify-content:center;gap:9px;font-size:17px;color:var(--red)}
.client i{width:16px;height:16px;border-radius:50%;background:var(--red);display:block}

/* footer */
.site-footer{position:absolute;left:0;top:1907px;width:1200px;height:278px;background:var(--red);color:var(--white);text-align:center}
.foot-brand{width:1200px;left:0;top:28px;font-size:40px;font-weight:400}
.keep{width:1200px;left:0;top:92px;font-size:26px}
.social-foot{left:0;width:1200px;top:160px;display:flex;justify-content:center;gap:22px}
.social-foot span{width:46px;height:46px;border-radius:50%;display:block}
.copy{width:1200px;left:0;top:234px;font-size:13px}
</style>
</head>
<body>

<header class="site-header">
  <div class="abs brand">Clinora Services</div>
  <div class="abs social-top" aria-label="Social links"><span></span><span></span><span></span></div>
  <nav class="abs main-nav">
    <a class="active">Home</a><a>About</a><a>Call</a><a>Services</a><a>Contact</a>
  </nav>
  <div class="abs nav-phone">
    <svg width="26" height="26" viewBox="0 0 24 24" fill="none" stroke="#fff" stroke-width="2"><path d="M5 3h4l2 5-3 2a11 11 0 0 0 6 6l2-3 5 2v4a2 2 0 0 1-2 2A17 17 0 0 1 3 5a2 2 0 0 1 2-2z"/></svg>
    0800-555-0142
  </div>
</header>

<section class="hero">
  <svg class="abs slider-arrow" style="left:68px" width="20" height="50" viewBox="0 0 20 50"><path d="M18 2 2 25l16 23" fill="none" stroke="#e2e2e2" stroke-width="2"/></svg>
  <svg class="abs slider-arrow" style="left:1104px" width="20" height="50" viewBox="0 0 20 50"><path d="M2 2l16 23L2 48" fill="none" stroke="#e2e2e2" stroke-width="2"/></svg>
  <h1 class="abs">WE PROVIDE THE BEST <span class="line2"><span class="r">CLINORA</span> <span class="y">SERVICES</span></span></h1>
  <div class="abs btn-more">Read More</div>
  <div class="abs hero-visual" role="img" aria-label="Smiling doctor in a white coat holding a magnifying glass next to a smartphone"></div>
  <div class="abs slider-dots"><i></i><i></i><i></i></div>
</section>

<section class="features">
  <div class="feature">
    <svg viewBox="0 0 64 64" fill="none" stroke="#fff" stroke-width="2.5"><circle cx="32" cy="20" r="11"/><path d="M21 18h22M14 60c0-13 8-22 18-22s18 9 18 22"/><circle cx="24" cy="54" r="4"/><path d="M24 40v10M40 40v8"/></svg>
    <h3>DOCTOR <span class="y">SERVICES</span></h3>
    <p>Lorem ipsum dolor sit amet,<br>consectetuer adipiscing elit, sed diam<br>nonummy nibh euismod tincidunt ut la</p>
  </div>
  <div class="feature">
    <svg viewBox="0 0 64 64" fill="none" stroke="#fff" stroke-width="3"><rect x="20" y="2" width="24" height="60" rx="4"/><path d="M20 12h24M20 50h24"/><circle cx="32" cy="56" r="1.5" fill="#fff"/></svg>
    <h3>24/7 <span class="y">AVAILABILITY</span></h3>
    <p>Lorem ipsum dolor sit amet,<br>consectetuer adipiscing elit, sed diam<br>nonummy nibh euismod tincidunt ut la</p>
  </div>
  <div class="feature">
    <svg viewBox="0 0 84 64" fill="#fff"><path d="M2 14h50v8h14l14 16v16H2z"/><circle cx="20" cy="56" r="7" stroke="#c70d2e" stroke-width="3"/><circle cx="64" cy="56" r="7" stroke="#c70d2e" stroke-width="3"/><rect x="22" y="20" width="8" height="24" fill="#c70d2e"/><rect x="14" y="28" width="24" height="8" fill="#c70d2e"/><path d="M56 26h9l9 10H56z" fill="#c70d2e"/><rect x="24" y="4" width="8" height="8"/></svg>
    <h3>AMBULANCE <span class="y">SERVICES</span></h3>
    <p>Lorem ipsum dolor sit amet,<br>consectetuer adipiscing elit, sed diam<br>nonummy nibh euismod tincidunt ut la</p>
  </div>
</section>

<section class="info">
  <h2 class="abs sec-title why-title">WHY US
    <svg width="38" height="42" viewBox="0 0 38 42"><path d="M19 42 8 30A18 18 0 1 1 30 30z" fill="#c70d2e"/><text x="19" y="26" text-anchor="middle" font-family="Roboto,Arial,sans-serif" font-weight="700" font-size="22" fill="#fff">?</text></svg>
  </h2>
  <div class="abs why-item" style="top:102px">
    <div class="disc"><svg width="40" height="46" viewBox="0 0 40 46" fill="none" stroke="#fff" stroke-width="2.5"><rect x="3" y="6" width="34" height="38" rx="2"/><rect x="13" y="2" width="14" height="8" fill="#c70d2e"/><path d="M9 20l3 3 5-5M9 32l3 3 5-5M22 21h9M22 33h9"/></svg></div>
    <div><h4>Appointment</h4><p>Lorem ipsum dolor sit amet, consectetuer<br>adipiscing elit, sed diam ut laoreet dolore</p></div>
  </div>
  <div class="abs why-item" style="top:213px">
    <div class="disc"><svg width="44" height="44" viewBox="0 0 44 44" fill="none" stroke="#fff" stroke-width="2.5"><path d="M8 4v12a9 9 0 0 0 18 0V4"/><path d="M17 25v6a9 9 0 0 0 18 0v-6"/><circle cx="35" cy="21" r="4"/></svg></div>
    <div><h4>Medical</h4><p>magna aliquam erat volutpat. Ut wisi enim ad<br>minim veniam, quis nostrud nisl ut a</p></div>
  </div>
  <div class="abs why-item" style="top:324px">
    <div class="disc"><svg width="46" height="30" viewBox="0 0 46 30" fill="none" stroke="#fff" stroke-width="2.5"><path d="M2 16h12l4-10 6 20 5-14 3 4h12"/></svg></div>
    <div><h4>Services</h4><p>Lorem ipsum dolor sit amet, consectetuer<br>adipiscing elit, sed diam ut laoreet dolore</p></div>
  </div>

  <h2 class="abs sec-title faq-title">FAQ'S
    <svg width="46" height="40" viewBox="0 0 46 40"><path d="M23 3C12 3 4 10 4 18c0 5 3 9 7 12l-3 8 10-5c2 1 3 1 5 1 11 0 19-7 19-16S34 3 23 3z" fill="none" stroke="#c70d2e" stroke-width="4"/></svg>
  </h2>
  <div class="abs faq" style="top:102px">
    <div class="faq-row"><div class="toggle">&minus;</div><div class="q">nonummy nibh euismod tincidun ?</div></div>
    <div class="faq-open">Lorem ipsum dolor sit amet, consectetuer adipiscing elit, sed diamt ut laoreet dolore magna aliquam erat volutpat. Ut wisi enim ad minim veniam, quis nostrud nisl ut a</div>
    <div class="faq-row"><div class="toggle">+</div><div class="q">exerci tation ullamcorper lobortis ?</div></div>
    <div class="faq-row"><div class="toggle">+</div><div class="q">velit esse molestiesc consequat ?</div></div>
    <div class="faq-row"><div class="toggle">+</div><div class="q">exerci tation ullamcorper lobortis ?</div></div>
  </div>
</section>

<section class="services">
  <h2 class="abs center-title" style="top:26px"><span class="r">CLINORA</span> <span class="y">SERVICES</span></h2>
  <div class="abs card" style="left:173px">
    <div class="photo" role="img" aria-label="Senior doctor reviewing notes in a bright clinic" style="background:linear-gradient(160deg,#f4f5f6,#c9cfd4 70%,#9aa3aa)"></div>
    <p>Lorem ipsum dolor sit amet, consectetuer<br>adipiscing elit, sed diamt ut laoreet dolore</p>
  </div>
  <div class="abs card" style="left:472px">
    <div class="photo" role="img" aria-label="Doctor talking with a patient in an office" style="background:linear-gradient(160deg,#eef1f3,#c7d3dc 60%,#8fa4b4)"></div>
    <p>Lorem ipsum dolor sit amet, consectetuer<br>adipiscing elit, sed diamt ut laoreet dolore</p>
  </div>
  <div class="abs card" style="left:772px">
    <div class="photo" role="img" aria-label="Doctor checking on a patient in a hospital bed" style="background:linear-gradient(160deg,#f2f4f6,#cfd9e2 60%,#8ea3b6)"></div>
    <p>Lorem ipsum dolor sit amet, consectetuer<br>adipiscing elit, sed diamt ut laoreet dolore</p>
  </div>
</section>

<section class="clients">
  <h2 class="abs center-title" style="top:22px"><span class="r">Our</span> <span class="y">Clients</span></h2>
  <div class="abs client" style="left:175px"><i></i>Veltra Tours</div>
  <div class="abs client" style="left:402px"><i></i>Nomedi Health</div>
  <div class="abs client" style="left:630px"><i></i>Cardiva Center</div>
  <div class="abs client" style="left:852px"><i></i>Orlume Wellness</div>
</section>

<footer class="site-footer">
  <div class="abs foot-brand">Clinora Services</div>
  <div class="abs keep">KEEP IN TOUCH</div>
  <div class="abs social-foot" aria-label="Social links">
    <span style="background:#3b4f9a"></span><span style="background:#3fa6dd"></span><span style="background:#2b6fa8"></span>
  </div>
  <div class="abs copy">Copyright © 2014. ClinoraServices . All Right Reserved.</div>
</footer>

</body>
</html>
```